Letterhead Design Project

I need letterhead designed for my law firm. It would also be used for web based stuff as well.

Industry/Entity Type

Law Firm

```html
<!DOCTYPE html>
<html lang="en">
<head>
<meta charset="utf-8">
<title>Harwell &amp; Lee Law Firm — Letterhead</title>
<link rel="stylesheet" href="https://fonts.googleapis.com/css2?family=Cinzel:wght@600&family=Arimo:wght@400&display=swap">
<style>
  :root {
    --paper-light: #fbfbfb;
    --paper-edge: #d9d9db;
    --ink-dark: #333333;
    --ink-faint: #c9cdd4;
    --swoosh-blue: #87aacd;
    --swoosh-pale: #dfe5ec;
    --footer-dark: #232323;
    --footer-navy: #2c3a55;
    --accent-yellow: #f2e316;
    --footer-text: #ffffff;
    --mark-grey: #b9b9bb;
  }
  html, body { margin: 0; padding: 0; overflow: hidden; }
  .letterhead {
    position: relative;
    width: 927px;
    height: 1200px;
    overflow: hidden;
    background: radial-gradient(ellipse 620px 720px at 470px 600px, var(--paper-light) 0%, #f1f1f2 55%, var(--paper-edge) 100%);
    font-family: "Arimo", Arial, sans-serif;
  }
  .brand-head {
    position: absolute;
    top: 48px;
    left: 0;
    width: 100%;
    text-align: center;
    font-family: "Cinzel", Georgia, serif;
    font-weight: 600;
    color: var(--ink-dark);
    letter-spacing: 1px;
  }
  .brand-head .brand-mark {
    display: block;
    width: 62px;
    height: 62px;
    margin: 0 auto 8px;
    border-radius: 50%;
    background: var(--mark-grey);
  }
  .brand-head .brand-name { display: block; font-size: 25px; line-height: 1.2; }
  .center-emblem {
    position: absolute;
    top: 560px;
    left: 0;
    width: 100%;
    text-align: center;
    font-family: "Cinzel", Georgia, serif;
    font-weight: 600;
    font-size: 56px;
    color: var(--ink-faint);
    letter-spacing: 2px;
  }
  .swooshes { position: absolute; left: 0; top: 0; }
  .footer {
    position: absolute;
    left: 0;
    bottom: 0;
    width: 927px;
    height: 105px;
    display: flex;
    color: var(--footer-text);
  }
  .footer-left {
    width: 462px;
    background: var(--footer-dark);
    position: relative;
  }
  .footer-right {
    flex: 1;
    background: var(--footer-navy);
    position: relative;
  }
  .footer-firm {
    position: absolute;
    left: 30px;
    top: 30px;
    width: 116px;
    text-align: center;
    color: var(--accent-yellow);
    font-size: 16px;
    line-height: 19px;
  }
  .footer-address {
    position: absolute;
    right: 74px;
    top: 28px;
    text-align: right;
    font-size: 16.5px;
    line-height: 21px;
  }
  .footer-mark {
    position: absolute;
    left: 428px;
    top: 28px;
    width: 66px;
    height: 50px;
    display: flex;
    align-items: center;
    justify-content: center;
    font-size: 13px;
    color: var(--mark-grey);
    z-index: 2;
  }
  .contact-list {
    position: absolute;
    left: 100px;
    top: 18px;
    margin: 0;
    padding: 0;
    list-style: none;
    font-size: 16.5px;
    line-height: 23px;
  }
  .contact-list li { display: flex; align-items: center; }
  .contact-list .icon { width: 18px; height: 16px; margin-right: 22px; display: inline-flex; justify-content: center; }
  .contact-list .web-icon { font-weight: 700; font-size: 19px; line-height: 16px; }
</style>
</head>
<body>
<main class="letterhead">
  <header class="brand-head">
    <span class="brand-mark" aria-hidden="true"></span>
    <span class="brand-name">Harwell &amp; Lee Law Firm</span>
  </header>

  <div class="center-emblem">Harwell &amp; Lee</div>

  <svg class="swooshes" width="927" height="1200" viewBox="0 0 927 1200" aria-hidden="true">
    <defs>
      <linearGradient id="swoosh-fill" x1="0" y1="0" x2="1" y2="0">
        <stop offset="0" stop-color="var(--swoosh-pale)" stop-opacity="0.3"/>
        <stop offset="0.55" stop-color="#b3c6da"/>
        <stop offset="1" stop-color="var(--swoosh-blue)"/>
      </linearGradient>
    </defs>
    <path class="swoosh swoosh-upper" fill="url(#swoosh-fill)"
          d="M60 1072 Q640 930 927 570 L927 772 Q640 990 60 1072 Z"/>
    <path class="swoosh swoosh-lower" fill="url(#swoosh-fill)"
          d="M80 1088 Q660 1010 927 830 L927 905 Q660 1045 80 1088 Z"/>
  </svg>

  <footer class="footer">
    <div class="footer-left">
      <div class="footer-firm">Harwell &amp; Lee<br>Law Firm</div>
      <address class="footer-address" style="font-style:normal">218 Linden Court Avenue<br>Fairview, NY 12904</address>
    </div>
    <div class="footer-mark">Harwell &amp; Lee</div>
    <div class="footer-right">
      <ul class="contact-list">
        <li>
          <span class="icon"><svg width="16" height="12" viewBox="0 0 16 12" aria-hidden="true"><rect x="0.7" y="0.7" width="14.6" height="10.6" fill="none" stroke="#fff" stroke-width="1.4"/><path d="M1 1 L8 7 L15 1" fill="none" stroke="#fff" stroke-width="1.4"/></svg></span>
          info@harwell|lee.com
        </li>
        <li>
          <span class="icon"><svg width="17" height="14" viewBox="0 0 17 14" aria-hidden="true"><path d="M1 5 Q8.5 -1 16 5 L13 6 L12 4 Q8.5 3 5 4 L4 6 Z" fill="#fff"/><rect x="3" y="7" width="11" height="6" rx="2" fill="#fff"/><circle cx="8.5" cy="10" r="1.6" fill="var(--footer-navy)"/></svg></span>
          01 555 010 27
        </li>
        <li>
          <span class="icon web-icon">e</span>
          www.harwell|lee.com
        </li>
      </ul>
    </div>
  </footer>
</main>
</body>
</html>
```